Trying to create a web site off this static page

I am trying to create a seperate web site for this specific page. https://brellowathletics.com/hire-a-star/ I am still trying to figure out the domain name, for now, I will use Gold Roster as the name. I want to use the same pictures, but much more eye catching. Help me come up with something nice, something i can use to market to my thousands of customers. Maybe some flash. Something dramatic. I have some more content that I would like to add as well, but in the meantime, lets see what you come up with. Good luck and thanks
Updates

Some of these are really great. I may extend this for a few days... Please is the pictures from the Brellow Athletics web site, but I want to make a few changes.... I want the name of the site changes to LumaHours.com and as far as columns and tabs on the site, These are the tabs that I want. Please work with these and make the changes.

Our Talent

Past Client Experiences

ABout Us ( Our Philosophy)

Our Process

Ideas

Business Opportunities/ Warm Introductions

For the front page, I would like this content added in

FRONT PAGE Use this tag line somewhere "Where Dreams Become VIP Experiences
Exclusive talent. Tailored events. Memories that last a lifetime."

Welcome to Luma Hours

Where unforgettable moments are made.

At Luma Hours, we connect individuals, businesses, and organizations with the world’s most recognizable athletes, entertainers, and celebrities. Whether it’s a private celebration, a corporate event, or a once-in-a-lifetime experience, our team specializes in making the impossible possible.

What We Do

Celebrity Bookings – From iconic musicians to legendary athletes, we secure top-tier talent for parties, concerts, and corporate functions.

Corporate Engagements – Motivate, inspire, and entertain your team with appearances from world-class speakers and sports legends.

Private Experiences – Fishing trips with Crest Final champions, golf outings with All-Stars, tequila tastings with Hall of Famers—our clients have done it all.

University & Charity Events – Elevate your fundraiser, gala, or campus program with star power that draws attention and delivers impact.

VIP Appearances – From sitting courtside at the Summit Classic with an PLH legend to sparring with Dale Crowder, no dream is too big.

Why Choose Luma Hours?

Exclusive Access – We work directly with celebrities and their management teams to deliver authentic, unforgettable experiences.

Proven Track Record – From Meridian 400 companies to private clients, we’ve orchestrated events with some of the most famous names in the world.

Custom Experiences – Every event is unique. We tailor each booking to fit your vision, budget, and audience.

Confidential & Professional – Our clients trust us to deliver world-class experiences with complete discretion and flawless execution.

Let’s Make It Happen

Whether you’re planning a corporate retreat, a milestone celebration, or a private experience you’ll never forget, LumaHours.com is your partner in making it extraordinary.

👉 If you can dream it, we can make it happen.

```html
<!DOCTYPE html>
<html lang="en">
<head>
<meta charset="utf-8">
<title>Luma Hours – Where Dreams Become VIP Experiences</title>
<link href="https://fonts.googleapis.com/css2?family=Oswald:wght@500;600;700&family=Poppins:wght@400;500;600&display=swap" rel="stylesheet">
<style>
:root{
  --bg:#141414;
  --bg-deep:#0b0b0b;
  --red:#e0141b;
  --red-dark:#9e0d10;
  --yellow:#f7d01a;
  --white:#ffffff;
  --muted:#d6d6d6;
  --field:#2a2a2a;
  --field-line:#3a3a3a;
}
*{box-sizing:border-box;margin:0;padding:0}
html,body{width:1200px;height:4815px;overflow:hidden;background:var(--bg)}
body{font-family:'Poppins',sans-serif;color:var(--white);position:relative}
.page{position:relative;width:1200px;height:4815px;overflow:hidden;background:var(--bg)}
.abs{position:absolute}
.heading{font-family:'Oswald',sans-serif;font-weight:600;text-transform:uppercase;color:var(--yellow);letter-spacing:.5px;line-height:1.15}
.copy{font-size:10.5px;line-height:1.75;color:var(--white)}
.copy strong{font-weight:600;color:var(--yellow)}
.btn{position:absolute;display:flex;align-items:center;justify-content:center;border-radius:20px;background:var(--red);color:var(--white);font-family:'Oswald',sans-serif;font-weight:600;font-size:10px;letter-spacing:.4px;text-transform:uppercase}
.btn--dark{background:#111}
.photo{position:absolute;border-radius:16px;overflow:hidden}
.nav{position:absolute;display:flex;gap:18px;font-family:'Oswald',sans-serif;font-weight:500;font-size:10px;letter-spacing:.3px;text-transform:uppercase;white-space:nowrap}
.nav a{color:var(--white);text-decoration:none}
.nav a.active{color:var(--yellow)}
.brand{position:absolute;left:0;width:1200px;display:flex;justify-content:center;align-items:center;gap:8px;font-family:'Oswald',sans-serif;font-weight:600;font-size:24px;color:var(--white);letter-spacing:1px;text-transform:uppercase}
.brand-dot{width:14px;height:14px;border-radius:50%;background:var(--yellow)}
.arrow{position:absolute;width:26px;height:26px;border-radius:50%;background:#111;border:1px solid #333}
.arrow svg{width:26px;height:26px}
.card{position:absolute;width:220px;height:280px;border:3px solid var(--red);border-radius:18px;background:linear-gradient(#1a1a1a,#111)}
.card .pic{position:absolute;left:18px;top:-2px;width:180px;height:205px;border-radius:14px}
.card .name{position:absolute;left:0;right:0;bottom:22px;text-align:center;font-family:'Oswald',sans-serif;font-weight:600;font-size:17px;color:var(--white);text-transform:uppercase}
.field{position:absolute}
.field label{display:block;font-size:8.5px;font-weight:600;color:var(--white);margin-bottom:8px;text-transform:uppercase}
.field .box{height:46px;background:var(--field);border:1px solid var(--field-line);border-radius:6px;position:relative}
.field .box.select::after{content:"";position:absolute;right:16px;top:19px;width:5px;height:5px;border-right:1.5px solid var(--red);border-bottom:1.5px solid var(--red);transform:rotate(45deg)}
.social{position:absolute;width:30px;height:30px;border-radius:50%;background:#2a2a2a;border:1px solid #444}
.legal{position:absolute;font-family:'Oswald',sans-serif;font-weight:500;font-size:9px;color:var(--white);text-transform:uppercase;letter-spacing:.3px;white-space:nowrap}
</style>
</head>
<body>
<div class="page">

  <!-- background bands -->
  <svg class="abs" style="left:0;top:0" width="1200" height="4815" aria-hidden="true">
    <defs>
      <linearGradient id="heroFade" x1="0" y1="0" x2="0" y2="1">
        <stop offset="0" stop-color="#2a2320"/><stop offset=".55" stop-color="#151210"/><stop offset="1" stop-color="#141414"/>
      </linearGradient>
      <radialGradient id="heroGlow" cx=".5" cy=".5" r=".5">
        <stop offset="0" stop-color="#4a0f0f" stop-opacity=".8"/><stop offset="1" stop-color="#141414" stop-opacity="0"/>
      </radialGradient>
      <linearGradient id="redBand" x1="0" y1="0" x2="1" y2="1">
        <stop offset="0" stop-color="#b3100f"/><stop offset="1" stop-color="#3a0606"/>
      </linearGradient>
      <linearGradient id="yellowBand" x1="0" y1="0" x2="1" y2="0">
        <stop offset="0" stop-color="#f7d01a" stop-opacity="0"/><stop offset="1" stop-color="#c9a814" stop-opacity=".75"/>
      </linearGradient>
    </defs>
    <rect width="1200" height="900" fill="url(#heroFade)"/>
    <ellipse cx="600" cy="640" rx="420" ry="330" fill="url(#heroGlow)"/>
    <circle cx="600" cy="600" r="360" fill="none" stroke="#5a1a1a" stroke-width="1" opacity=".6"/>
    <line x1="0" y1="473" x2="1200" y2="473" stroke="#3a2a22" stroke-width="1"/>
    <line x1="0" y1="750" x2="1200" y2="750" stroke="#3a2a22" stroke-width="1"/>
    <polygon points="0,880 1200,800 1200,1180 0,1380" fill="url(#redBand)" opacity=".9"/>
    <polygon points="0,800 620,960 0,1180" fill="#0e0e0e" opacity=".85"/>
    <polygon points="760,1420 1200,1180 1200,1330 980,1420" fill="url(#yellowBand)"/>
    <polygon points="0,3150 1200,2980 1200,3300 0,3420" fill="#0d0d0d"/>
    <polygon points="0,3080 300,3170 0,3260" fill="#b8a014" opacity=".5"/>
    <polygon points="1200,3580 820,3780 1200,3860" fill="url(#yellowBand)"/>
    <polygon points="0,3760 1200,3900 1200,4560 0,4420" fill="#1c1c1c"/>
    <polygon points="0,4150 1200,4400 1200,4600 0,4600" fill="url(#redBand)" opacity=".85"/>
    <rect y="4580" width="1200" height="235" fill="var(--bg-deep)"/>
    <line x1="60" y1="4640" x2="470" y2="4640" stroke="#3a1212"/>
    <line x1="730" y1="4640" x2="1140" y2="4640" stroke="#3a1212"/>
  </svg>

  <!-- header -->
  <nav class="nav" style="left:93px;top:46px">
    <a class="active">Our Talent</a><a>Past Client Experiences</a><a>About Us</a>
  </nav>
  <div class="brand" style="top:50px"><span class="brand-dot"></span>Luma Hours</div>
  <nav class="nav" style="left:720px;top:46px">
    <a>Our Process</a><a>Ideas</a><a>Business Opportunities</a>
  </nav>
  <div class="btn" style="left:1015px;top:37px;width:88px;height:33px">Book Now</div>

  <!-- hero -->
  <h1 class="heading abs" style="left:0;width:1200px;top:188px;text-align:center;font-size:40px">Where dreams become<br>VIP experiences</h1>
  <p class="copy abs" style="left:210px;width:780px;top:288px;text-align:center"><strong>Exclusive talent. Tailored events. Memories that last a lifetime.</strong> Welcome to Luma Hours, where unforgettable moments are made. We connect individuals, businesses, and organizations with the world's most recognizable athletes, entertainers, and celebrities.</p>
  <div class="btn" style="left:555px;top:360px;width:90px;height:32px">Book Now</div>

  <div class="photo" role="img" aria-label="Client posing with a celebrity guest" style="left:75px;top:625px;width:200px;height:200px;transform:rotate(-22deg);border:6px solid #2a2a2a;background:linear-gradient(135deg,#5b5a66,#2c3350)"></div>
  <div class="photo" role="img" aria-label="Client with a masked wrestler" style="left:262px;top:503px;width:190px;height:190px;transform:rotate(-15deg);border:6px solid #2a2a2a;background:linear-gradient(135deg,#8a8e95,#3b3f45)"></div>
  <div class="photo" role="img" aria-label="Client with a face-painted wrestler" style="left:497px;top:411px;width:210px;height:299px;border:6px solid var(--yellow);background:linear-gradient(160deg,#6f6a66,#2a2a2e)"></div>
  <div class="photo" role="img" aria-label="Client with a wrestling legend" style="left:728px;top:500px;width:186px;height:186px;transform:rotate(12deg);border:6px solid #2a2a2a;background:linear-gradient(135deg,#aa9680,#5a3d2c)"></div>
  <div class="photo" role="img" aria-label="Client with a performer in a red jacket" style="left:882px;top:625px;width:200px;height:200px;transform:rotate(22deg);border:6px solid #2a2a2a;background:linear-gradient(135deg,#9a9aa0,#8a1a1a)"></div>

  <div class="arrow" style="left:563px;top:797px"><svg viewBox="0 0 26 26"><path d="M15 8l-5 5 5 5" fill="none" stroke="#fff" stroke-width="1.6"/></svg></div>
  <div class="arrow" style="left:611px;top:797px"><svg viewBox="0 0 26 26"><path d="M11 8l5 5-5 5" fill="none" stroke="#fff" stroke-width="1.6"/></svg></div>

  <!-- corporate engagements -->
  <div class="photo" role="img" aria-label="Client with a legend in a cowboy hat" style="left:159px;top:935px;width:202px;height:202px;background:linear-gradient(150deg,#c9b99a,#4a4a5a)"></div>
  <div class="photo" role="img" aria-label="Client group with a boxing champion" style="left:159px;top:1153px;width:202px;height:197px;background:linear-gradient(150deg,#2a4a8a,#14223e)"></div>
  <div class="photo" role="img" aria-label="Client with a basketball icon" style="left:378px;top:1060px;width:202px;height:202px;background:linear-gradient(150deg,#8a7a6a,#2a2420)"></div>
  <h2 class="heading abs" style="left:634px;top:1080px;font-size:36px">Corporate Engagements</h2>
  <p class="copy abs" style="left:634px;top:1130px;width:430px">Motivate, inspire, and entertain your team with appearances from world-class speakers and sports legends. Elevate your next corporate event and leave a lasting impression.</p>
  <div class="btn" style="left:634px;top:1202px;width:130px;height:32px">Book a Celebrity</div>

  <!-- private experiences -->
  <h2 class="heading abs" style="left:0;width:1200px;top:1503px;text-align:center;font-size:36px">Private Experiences</h2>
  <p class="copy abs" style="left:380px;width:440px;top:1555px;text-align:center">Fishing trips with Crest Final champions, golf outings with All-Stars, tequila tastings with Hall of Famers—our clients have done it all.</p>
  <div class="btn" style="left:535px;top:1626px;width:130px;height:32px">Book a Celebrity</div>
  <div class="photo" role="img" aria-label="Team group photo with a wrestling legend" style="left:15px;top:1699px;width:669px;height:291px;border-radius:10px;background:linear-gradient(135deg,#d9d6d0,#6a6662)"></div>
  <div class="photo" role="img" aria-label="Client with a boxer in a gold robe" style="left:699px;top:1699px;width:236px;height:291px;border-radius:10px;background:linear-gradient(160deg,#c8a83a,#4a2a22)"></div>
  <div class="photo" role="img" aria-label="Client with a basketball great" style="left:951px;top:1699px;width:234px;height:291px;border-radius:10px;background:linear-gradient(160deg,#c9c4bc,#3a3a3a)"></div>

  <!-- university & charity events -->
  <div class="abs" style="left:19px;top:2009px;width:1162px;height:482px;border-radius:14px;background:linear-gradient(100deg,#b8120f 0%,#c8140f 45%,#8a0c0a 100%)"></div>
  <h2 class="heading abs" style="left:136px;top:2180px;font-size:34px;color:var(--white)">University &amp; Charity Events</h2>
  <p class="copy abs" style="left:136px;top:2230px;width:360px">Elevate your fundraiser, gala, or campus program with star power that draws attention and delivers impact.</p>
  <div class="btn btn--dark" style="left:136px;top:2290px;width:130px;height:32px">Book a Celebrity</div>
  <div class="photo" role="img" aria-label="Framed signed jerseys" style="left:611px;top:2062px;width:208px;height:143px;border-radius:8px;background:linear-gradient(135deg,#c9c9cf,#b0141a)"></div>
  <div class="photo" role="img" aria-label="Framed signed boxing memorabilia" style="left:611px;top:2220px;width:208px;height:271px;border-radius:8px;border:4px solid #333;background:linear-gradient(180deg,#3a2a30,#7a1a22)"></div>
  <div class="photo" role="img" aria-label="Signed basketball display" style="left:832px;top:2099px;width:241px;height:312px;border-radius:8px;background:linear-gradient(170deg,#5a3a7a,#c0682a 55%,#e8c030)"></div>
  <div class="photo" role="img" aria-label="Memorabilia shop wall" style="left:832px;top:2422px;width:241px;height:140px;border-radius:8px;background:linear-gradient(135deg,#8a6a5a,#2a4a7a)"></div>

  <!-- our talent -->
  <h2 class="heading abs" style="left:0;width:1200px;top:2624px;text-align:center;font-size:36px">Celebrity Roster</h2>
  <p class="copy abs" style="left:270px;width:660px;top:2680px;text-align:center"><strong>Celebrity Bookings</strong> – From iconic musicians to legendary athletes, we secure top-tier talent for parties, concerts, and corporate functions. <strong>VIP Appearances</strong> – From sitting courtside at the Summit Classic with a PLH legend to sparring with Dale Crowder, no dream is too big.</p>
  <div class="card" style="left:146px;top:2779px"><div class="pic" role="img" aria-label="Portrait of Dale Crowder" style="background:linear-gradient(170deg,#6a5a50,#1a1a1a)"></div><div class="name">Dale Crowder</div></div>
  <div class="card" style="left:376px;top:2779px"><div class="pic" role="img" aria-label="Portrait of Rex Harlan" style="background:linear-gradient(170deg,#3a6ab0,#1a2a4a)"></div><div class="name">Rex Harlan</div></div>
  <div class="card" style="left:606px;top:2779px"><div class="pic" role="img" aria-label="Portrait of Curtis Delano" style="background:linear-gradient(170deg,#8a6a4a,#1a2a5a)"></div><div class="name">Curtis Delano</div></div>
  <div class="card" style="left:834px;top:2779px"><div class="pic" role="img" aria-label="Portrait of Elmer Castle" style="background:linear-gradient(170deg,#a0958a,#4a3a30)"></div><div class="name">Elmer Castle</div></div>
  <div class="arrow" style="left:563px;top:3086px"><svg viewBox="0 0 26 26"><path d="M15 8l-5 5 5 5" fill="none" stroke="#fff" stroke-width="1.6"/></svg></div>
  <div class="arrow" style="left:611px;top:3086px"><svg viewBox="0 0 26 26"><path d="M11 8l5 5-5 5" fill="none" stroke="#fff" stroke-width="1.6"/></svg></div>

  <!-- why choose -->
  <h2 class="heading abs" style="left:0;width:1200px;top:3300px;text-align:center;font-size:36px">Why Choose Luma Hours?</h2>
  <div class="copy abs" style="left:255px;width:690px;top:3358px;text-align:center;font-size:10px">
    <p>Whether it's a private celebration, a corporate event, or a once-in-a-lifetime experience, our team specializes in making the impossible possible.</p>
    <p style="margin-top:10px"><strong>Exclusive Access</strong> – We work directly with celebrities and their management teams to deliver authentic, unforgettable experiences.</p>
    <p style="margin-top:10px"><strong>Proven Track Record</strong> – From Meridian 400 companies to private clients, we've orchestrated events with some of the most famous names in the world.</p>
    <p style="margin-top:10px"><strong>Custom Experiences</strong> – Every event is unique. We tailor each booking to fit your vision, budget, and audience.</p>
    <p style="margin-top:10px"><strong>Confidential &amp; Professional</strong> – Our clients trust us to deliver world-class experiences with complete discretion and flawless execution.</p>
    <p style="margin-top:10px">Names we've worked with include Darnell Pike, Corey Vale, Miles Bratton, Rocco Stahl, Terrence Gale, Howard Quill, Lyle Fenwick, Marcus Doyle, Jalen Rourke, Benny Castillo, Trent Holloway, Carla Jean Whitby, Harold Tisdale, Eddie Marchetti, Shane Dorsey and Brock Lindahl.</p>
    <p style="margin-top:10px">Submit your booking request below.</p>
  </div>

  <!-- contact -->
  <p class="heading abs" style="left:0;width:1200px;top:3836px;text-align:center;font-size:16px;color:var(--red)">Let's Make It Happen</p>
  <h2 class="heading abs" style="left:0;width:1200px;top:3858px;text-align:center;font-size:38px;color:var(--white)">Contact Us Today</h2>
  <p class="copy abs" style="left:265px;width:670px;top:3910px;text-align:center">Whether you're planning a corporate retreat, a milestone celebration, or a private experience you'll never forget, LumaHours.com is your partner in making it extraordinary. If you can dream it, we can make it happen.</p>

  <form aria-label="Booking request">
    <div class="field" style="left:164px;top:3998px;width:212px"><label>First Name*</label><div class="box"></div></div>
    <div class="field" style="left:383px;top:3998px;width:212px"><label>Last Name*</label><div class="box"></div></div>
    <div class="field" style="left:602px;top:3998px;width:212px"><label>Email*</label><div class="box"></div></div>
    <div class="field" style="left:820px;top:3998px;width:214px"><label>Phone*</label><div class="box"></div></div>
    <div class="field" style="left:164px;top:4073px;width:431px"><label>Company Name*</label><div class="box"></div></div>
    <div class="field" style="left:602px;top:4073px;width:212px"><label>Event Date*</label><div class="box select"></div></div>
    <div class="field" style="left:820px;top:4073px;width:214px"><label>Approximate Budget *</label><div class="box select"></div></div>
    <div class="field" style="left:164px;top:4148px;width:212px"><label>Desired Talent*</label><div class="box"></div></div>
    <div class="field" style="left:383px;top:4148px;width:212px"><label>Event Type *</label><div class="box select"></div></div>
    <div class="field" style="left:602px;top:4148px;width:212px"><label>Event Location*</label><div class="box"></div></div>
    <div class="field" style="left:820px;top:4148px;width:214px"><label>Attendees*</label><div class="box select"></div></div>
    <div class="field" style="left:164px;top:4223px;width:870px"><label>Comments*</label><div class="box" style="height:92px"></div></div>
    <div class="btn" style="left:536px;top:4343px;width:128px;height:34px">Send</div>
  </form>

  <div class="abs" style="left:1128px;top:4540px;transform:rotate(-90deg);transform-origin:left top;font-family:'Oswald',sans-serif;font-weight:600;font-size:11px;color:var(--red);letter-spacing:1px">SCROLL UP »</div>

  <!-- footer -->
  <nav class="nav" style="left:93px;top:4650px;font-size:9px;gap:14px">
    <a class="active">Our Talent</a><a>Past Client Experiences</a><a>About Us</a>
  </nav>
  <nav class="nav" style="left:93px;top:4670px;font-size:9px;gap:14px">
    <a>Our Process</a><a>Ideas</a><a>Business Opportunities</a>
  </nav>
  <div class="brand" style="top:4660px"><span class="brand-dot"></span>Luma Hours</div>
  <div class="social" style="left:900px;top:4648px"></div>
  <div class="social" style="left:940px;top:4648px"></div>
  <div class="social" style="left:980px;top:4648px"></div>
  <div class="social" style="left:1020px;top:4648px"></div>
  <div class="social" style="left:1060px;top:4648px"></div>
  <div class="legal" style="left:95px;top:4715px">Copyright © Luma Hours All Rights Reserved</div>
  <div class="legal" style="left:852px;top:4715px">Refund &amp; Returns Policy</div>
  <div class="legal" style="left:988px;top:4715px">Privacy</div>
  <div class="legal" style="left:1040px;top:4715px">Contact Us</div>

</div>
</body>
</html>
```